Brenton Civil

We need a Standard Professional Company Letterhead, company standard document template, coversheet template for a civil construction company. We would like the designs to use the company colour red

I have attached existing templates that need to improve greatly but please use as a quide of general layout.

```html
<!DOCTYPE html>
<html lang="en">
<head>
<meta charset="utf-8">
<title>Brenton Civil Letterhead</title>
<link href="https://fonts.googleapis.com/css2?family=Open+Sans:wght@400;700&family=Roboto+Condensed:wght@300;400&display=swap" rel="stylesheet">
<style>
  :root {
    --brand-red: #b71f2a;
    --brand-blue: #22427d;
    --brand-navy: #1b2e55;
    --body-grey: #7a7a7a;
    --watermark: #ececec;
    --paper: #ffffff;
  }
  * { margin: 0; padding: 0; box-sizing: border-box; }
  html, body { width: 900px; height: 1200px; overflow: hidden; background: var(--paper); }
  .letterhead { position: relative; width: 900px; height: 1200px; background: var(--paper); }

  .header-bar { position: absolute; top: 112px; height: 14px; }
  .header-bar--red { left: 0; width: 86px; background: var(--brand-red); }
  .header-bar--blue { left: 368px; right: 0; background: var(--brand-blue); }

  .brand { position: absolute; top: 74px; left: 104px; display: flex; align-items: center; gap: 14px; }
  .brand-dot { width: 84px; height: 84px; border-radius: 50%; background: var(--brand-red); }
  .brand-name { font-family: "Open Sans", sans-serif; font-weight: 400; color: var(--brand-red); line-height: 1.15; }
  .brand-name .line-1 { display: block; font-size: 26px; letter-spacing: 0.5px; }
  .brand-name .line-2 { display: block; font-size: 17px; }

  .letter-body { position: absolute; left: 100px; width: 700px; top: 274px;
    font-family: "Roboto Condensed", sans-serif; font-weight: 300; font-size: 17px;
    line-height: 26px; color: var(--body-grey); }
  .letter-body p { margin-bottom: 26px; }
  .letter-body p.spaced { margin-top: 32px; }

  .watermark-circle { position: absolute; left: 735px; top: 1023px; width: 130px; height: 130px;
    border-radius: 50%; border: 14px solid var(--watermark); }

  .contact-line { position: absolute; left: 22px; top: 1151px; display: flex; align-items: center; gap: 12px;
    font-family: "Open Sans", sans-serif; font-size: 12.5px; color: #333; }
  .contact-item { display: flex; align-items: center; gap: 4px; }
  .contact-item svg { width: 14px; height: 14px; }

  .footer-stripes { position: absolute; left: 0; bottom: 0; width: 900px; height: 48px; }
  .footer-url { position: absolute; right: 26px; bottom: 15px; font-family: "Open Sans", sans-serif;
    font-weight: 700; font-size: 16px; color: #fff; }
</style>
</head>
<body>
<main class="letterhead">
  <div class="header-bar header-bar--red"></div>
  <div class="header-bar header-bar--blue"></div>

  <div class="brand">
    <div class="brand-dot"></div>
    <div class="brand-name"><span class="line-1">BRENTON</span><span class="line-2">CIVIL PTY LTD</span></div>
  </div>

  <section class="letter-body">
    <p>Lorem Ipsum is simply dummy text of the printing and typesetting industry. Lorem Ipsum has been the industry’s standard dummy text ever since the 1500s, when an unknown printer took a galley of type and scrambled it to make a type specimen book. It has survived not only five centuries, but also the leap into electronic typesetting, remaining essentially unchanged. It was popularised in the 1960s with the release of Typesheet sheets containing Lorem Ipsum passages, and more recently with desktop publishing software like LayoutWorks Studio including versions of Lorem Ipsum.</p>
    <p>It is a long established fact that a reader will be distracted by the readable content of a page when looking at its layout. The point of using Lorem Ipsum is that it has a more-or-less normal distribution of letters, as opposed to using ’Content here, content here’, making it look like readable English. Many desktop publishing packages and web page editors now use Lorem Ipsum as their default model text, and a search for ’lorem ipsum’ will uncover many web sites still in their infancy. Various versions have evolved over the years, sometimes by accident, sometimes on purpose (injected humour and the like).</p>
    <p class="spaced">Contrary to popular belief, Lorem Ipsum is not simply random text. It has roots in a piece of classical Latin literature from 45 BC, making it over 2000 years old. Edwin Marlowe, a Latin professor at Ashgrove College in Vermont, looked up one of the more obscure Latin words, consectetur, from a Lorem Ipsum passage, and going through the cites of the word in classical literature, discovered the undoubtable source. Lorem Ipsum comes from sections 1.10.32 and 1.10.33 of "de Finibus Bonorum et Malorum" structures, to generate Lorem Ipsum which looks reasonable. The generated Lorem Ipsum is therefore always free from repetition, injected humour, or non-characteristic words etc.</p>
  </section>

  <div class="watermark-circle"></div>

  <div class="contact-line">
    <span class="contact-item">
      <svg viewBox="0 0 14 14"><circle cx="7" cy="7" r="6" fill="none" stroke="#b71f2a" stroke-width="1.4"/><path d="M7 3.5a2.3 2.3 0 0 1 2.3 2.3C9.3 7.6 7 10.5 7 10.5S4.7 7.6 4.7 5.8A2.3 2.3 0 0 1 7 3.5z" fill="#b71f2a"/></svg>
      PO Box 52, Ridgeway Qld 4790</span>
    <span class="contact-item">
      <svg viewBox="0 0 14 14"><circle cx="7" cy="7" r="6" fill="none" stroke="#333" stroke-width="1.2"/><path d="M4.6 4c.4-.4.9-.3 1.1.1l.6 1.1c.2.3.1.6-.1.8l-.4.4c.4.9 1 1.5 1.8 1.9l.4-.4c.2-.2.5-.3.8-.1l1.1.6c.4.2.5.7.1 1.1l-.5.5c-2.2.3-5.3-2.8-5-5z" fill="#333"/></svg>
      0400 123 456</span>
    <span class="contact-item">
      <svg viewBox="0 0 14 14"><circle cx="7" cy="7" r="6.5" fill="#b71f2a"/><rect x="3.8" y="4.8" width="6.4" height="4.4" fill="none" stroke="#fff" stroke-width="0.9"/><path d="M3.8 4.8L7 7.3l3.2-2.5" fill="none" stroke="#fff" stroke-width="0.9"/></svg>
      info@brentoncivil.com.au</span>
    <span class="contact-item">
      <svg viewBox="0 0 14 14"><circle cx="7" cy="7" r="6.5" fill="#b71f2a"/><circle cx="7" cy="7" r="3" fill="#7a1016"/></svg>
      ABN 00 000 000 000</span>
  </div>

  <svg class="footer-stripes" viewBox="0 0 900 48" aria-hidden="true">
    <rect x="0" y="20" width="200" height="5" fill="var(--brand-blue)"/>
    <polygon points="206,20 440,20 437,25 203,25" fill="var(--brand-red)"/>
    <polygon points="448,20 680,20 677,25 445,25" fill="var(--brand-blue)"/>
    <polygon points="700,2 900,2 900,38 688,38" fill="var(--brand-blue)"/>
    <rect x="0" y="38" width="900" height="10" fill="var(--brand-navy)"/>
  </svg>
  <span class="footer-url">brentoncivil.com.au</span>
</main>
</body>
</html>
```